Commercial construction contractor website.

We need a website that contains About Us, Contact info, Services, Project pictures and Industry News section

Target Market(s)

I'm building industral/flex spaces/commercial.

Industry/Entity Type

Commercial/industrial construction

Coding

Coded - Design and coding required

Number of Pages Required

5+ page

Font styles to use
Other font styles liked:
• The logo font is Microgramma Pro

Requirements
Must have
• Must have correct company name spelling: Dunmore Ridge Construction
Nice to have
• I do like to see our logo design implemented in the design
Should not have
• Please do not show big city pictures and business suit people. We are a commercial construction company

```html
<!DOCTYPE html>
<html lang="en">
<head>
<meta charset="utf-8">
<title>Dunmore Ridge Construction</title>
<link rel="stylesheet" href="https://fonts.googleapis.com/css2?family=Poppins:wght@400;500;600&family=Saira:wght@500;600;700&display=swap">
<style>
:root{
  --blue:#0b8fd3;
  --blue-deep:#0b4f9e;
  --navy:#153f78;
  --ink:#222;
  --muted:#6b6f75;
  --line:#d9dadd;
  --white:#fff;
}
*{box-sizing:border-box;margin:0;padding:0}
html,body{width:1200px;height:4225px;overflow:hidden;background:#fff}
body{font-family:"Poppins",sans-serif;color:var(--ink)}
.page{position:relative;width:1200px;height:4225px;overflow:hidden}
.abs{position:absolute}
svg{display:block}

/* top bar */
.topbar{left:0;top:0;width:1200px;height:36px;background:linear-gradient(90deg,#0a93d6,#0b7cc4);color:#fff;font-size:12px}
.topbar .item{position:absolute;top:10px;display:flex;align-items:center;gap:8px}

/* nav */
.nav{left:0;top:36px;width:1200px;height:62px;background:#fff;box-shadow:0 1px 4px rgba(0,0,0,.08)}
.brand{position:absolute;left:58px;top:12px;display:flex;align-items:center;gap:8px;color:var(--navy);font-family:"Saira",sans-serif;font-weight:700;font-size:14px;line-height:1.05;letter-spacing:.5px}
.brand .mark{width:22px;height:22px;background:var(--blue)}
.menu{position:absolute;left:470px;top:22px;display:flex;gap:32px;font-size:12px;color:#555}
.menu .active{color:var(--blue)}
.call{position:absolute;left:1033px;top:15px;font-size:11px;color:#777;line-height:1.3}
.call strong{display:block;font-size:14px;color:var(--navy);font-weight:600}

/* hero */
.hero-photo{left:0;top:98px;width:1200px;height:660px;clip-path:polygon(0 0,100% 0,100% 590px,600px 659px,213px 615px,0 652px);background:linear-gradient(100deg,#3a3d40 0%,#55575a 45%,#4d5a44 85%,#3f6a34 100%)}
.hero-title{left:0;top:282px;width:1200px;text-align:center;font-family:"Saira",sans-serif;font-weight:700;font-size:58px;line-height:64px;color:#2488dc;letter-spacing:.5px}
.hero-text{left:370px;top:420px;width:460px;text-align:center;color:#fff;font-size:12.5px;line-height:20px}
.btn{display:flex;align-items:center;justify-content:center;background:var(--blue);color:#fff;font-size:13px;font-weight:500;text-transform:uppercase}
.hero-btn{left:520px;top:502px;width:160px;height:36px;background:#0b7ec6}

/* section heads */
.eyebrow{font-size:11px;color:#444;text-transform:uppercase;display:flex;align-items:center;gap:10px}
.eyebrow::before{content:"";width:30px;height:1px;background:#444}
.sec-title{font-family:"Saira",sans-serif;font-weight:600;font-size:34px;color:var(--navy);text-transform:uppercase;line-height:1}
.center-head{left:0;width:1200px;text-align:center}
.center-head .eyebrow{justify-content:center}

/* about */
.about-box{left:144px;top:895px;width:941px;height:361px;border:1px solid var(--line)}
.about-copy{left:198px;top:940px;width:330px}
.about-copy p{font-size:12px;color:var(--muted);line-height:20px;margin-top:14px}
.checks{list-style:none;margin-top:12px}
.checks li{display:flex;gap:10px;font-size:12px;color:var(--muted);line-height:20px;margin-bottom:12px}
.checks svg{flex:none;margin-top:3px}

/* services */
.services-band{left:0;top:1331px;width:1200px;height:629px;clip-path:polygon(0 0,100% 0,100% 562px,600px 629px,0 562px);background:linear-gradient(180deg,#b7babd 0%,#cfd1d3 55%,#d8d9db 100%)}
.service{width:261px}
.service .pic{width:261px;height:246px;clip-path:polygon(0 0,100% 0,100% 185px,50% 246px,0 185px)}
.service h3{font-size:13.5px;font-weight:500;text-align:center;margin-top:36px;color:#222}
.service p{font-size:12px;line-height:20px;text-align:center;color:#444;margin-top:8px;padding:0 10px}

/* projects */
.proj-copy{left:140px;top:2446px;width:310px;font-size:12px;line-height:20px;color:#444}
.proj-btn{left:140px;top:2516px;width:160px;height:36px;background:#0a7fc5}

/* quality */
.quality-band{left:0;top:2672px;width:1200px;height:525px;clip-path:polygon(0 65px,600px 0,100% 65px,100% 100%,0 100%);background:linear-gradient(90deg,#c4c6c9 0%,#b3b6ba 50%,#8e9399 100%)}
.quality-copy{left:60px;top:2812px;width:400px}
.quality-copy p{font-size:12px;color:#fff;line-height:20px;margin-top:12px}
.stat{position:absolute;top:2975px;display:flex;align-items:center;gap:16px}
.stat .num{width:84px;height:82px;border:1px solid #fff;display:flex;align-items:center;justify-content:center;font-family:"Saira",sans-serif;font-weight:700;font-size:30px;color:var(--navy)}
.stat span{font-size:13px;font-weight:500;color:var(--navy);line-height:22px}
.quality-btn{left:59px;top:3077px;width:162px;height:35px}

/* news */
.card{width:270px;height:399px;background:#fff;box-shadow:0 2px 10px rgba(0,0,0,.12)}
.card .pic{height:215px;clip-path:polygon(0 0,100% 0,100% 185px,50% 215px,0 185px)}
.card .meta{display:flex;gap:22px;align-items:center;font-size:11px;color:#666;padding:32px 18px 0}
.card .meta span{display:flex;gap:6px;align-items:center}
.card h3{font-size:12px;font-weight:600;line-height:20px;padding:10px 18px 0;color:#222}
.card p{font-size:11.5px;line-height:20px;color:#777;padding:10px 18px 0}

/* footer */
.footer{left:0;top:3820px;width:1200px;height:352px;clip-path:polygon(0 89px,600px 0,100% 89px,100% 100%,0 100%);background:linear-gradient(100deg,#0a9ad8 0%,#0b73bf 50%,#0c4f9f 100%);color:#fff}
.foot-brand{left:62px;top:4030px;display:flex;align-items:center;gap:10px;font-family:"Saira",sans-serif;font-weight:700;font-size:20px;line-height:1.05;color:#fff;letter-spacing:.5px}
.foot-brand .mark{width:26px;height:26px;background:#fff;border-radius:50%}
.foot-col h4{font-size:15px;font-weight:500;margin-bottom:14px}
.foot-col ul{list-style:none}
.foot-col li{font-size:12px;height:30px}
.contact-list li{display:flex;gap:12px;align-items:center;height:52px}
.news-input{width:252px;height:36px;background:#fff;color:#777;font-size:11px;padding:11px 12px}
.news-btn{width:146px;height:35px;margin-top:16px;background:#0b5fae;font-size:12px}
.copyright{left:0;top:4172px;width:1200px;height:53px;background:#0c3f7c;color:#fff;font-size:11.5px;display:flex;align-items:center;justify-content:center}
</style>
</head>
<body>
<div class="page">

  <!-- top bar -->
  <div class="abs topbar">
    <div class="item" style="left:585px">
      <svg width="14" height="16" viewBox="0 0 14 16"><path d="M7 1a5 5 0 0 1 5 5c0 4-5 9-5 9S2 10 2 6a5 5 0 0 1 5-5z" fill="none" stroke="#fff" stroke-width="1.3"/><circle cx="7" cy="6" r="1.8" fill="none" stroke="#fff" stroke-width="1.2"/></svg>
      101-Lorem ipsum is dummy
    </div>
    <div class="item" style="left:832px">
      <svg width="18" height="13" viewBox="0 0 18 13"><rect x="1" y="1" width="16" height="11" fill="none" stroke="#fff" stroke-width="1.3"/><path d="M1 1l8 6 8-6" fill="none" stroke="#fff" stroke-width="1.3"/></svg>
      info@dunmoreridge.com
    </div>
    <div class="item" style="left:1044px;font-size:11px">
      <svg width="14" height="14" viewBox="0 0 14 14"><circle cx="7" cy="7" r="6" fill="none" stroke="#fff" stroke-width="1.2"/><path d="M1 7h12M7 1c-3 3-3 9 0 12M7 1c3 3 3 9 0 12" fill="none" stroke="#fff" stroke-width="1"/></svg>
      ENGLISH
      <svg width="10" height="6" viewBox="0 0 10 6"><path d="M0 0h10L5 6z" fill="#fff"/></svg>
    </div>
  </div>

  <!-- navigation -->
  <header class="abs nav">
    <div class="brand"><span class="mark"></span><span>DUNMORE RIDGE<br>CONSTRUCTION</span></div>
    <nav class="menu">
      <span class="active">Home</span><span>About Us</span><span>Services</span><span>Project</span><span>News</span><span>Contact Us</span>
    </nav>
    <svg class="abs" style="left:943px;top:24px" width="15" height="15" viewBox="0 0 15 15"><circle cx="6" cy="6" r="4.5" fill="none" stroke="#153f78" stroke-width="2"/><path d="M9.5 9.5L14 14" stroke="#153f78" stroke-width="2"/></svg>
    <svg class="abs" style="left:985px;top:17px" width="26" height="26" viewBox="0 0 26 26"><path d="M6 3l4 5-2 3c1 3 4 6 7 7l3-2 5 4-3 4C11 23 3 15 2 6z" fill="none" stroke="#153f78" stroke-width="2"/><path d="M15 4a7 7 0 0 1 7 7M15 8a3 3 0 0 1 3 3" fill="none" stroke="#153f78" stroke-width="1.6"/></svg>
    <div class="call">CALL US<strong>+1 555 014 7890</strong></div>
  </header>

  <!-- hero -->
  <div class="abs hero-photo" role="img" aria-label="Modern commercial interior lobby with seating and green living wall"></div>
  <h1 class="abs hero-title">WE BUILD YOUR<br>DREAM</h1>
  <p class="abs hero-text">Lorem Ipsum is simply dummy text of the printing and typesetting industry. Lorem Ipsum has been the industry's standard dummy text ever since the 1500s.</p>
  <div class="abs btn hero-btn">View all projects</div>

  <!-- about -->
  <section>
    <div class="abs about-box"></div>
    <svg class="abs" style="left:600px;top:895px" width="490" height="362" viewBox="0 0 490 362" role="img" aria-label="Construction crew in hard hats reviewing plans on site">
      <polygon points="256,0 16,361 485,361" fill="#c7a57a"/>
    </svg>
    <div class="abs about-copy">
      <div class="eyebrow">Dunmore Ridge Construction</div>
      <h2 class="sec-title" style="margin-top:20px">About Us</h2>
      <p>Lorem Ipsum is simply dummy text of the printing and typesetting industry. Lorem Ipsum has been the industry's</p>
      <ul class="checks">
        <li><svg width="14" height="14" viewBox="0 0 14 14"><circle cx="7" cy="7" r="6" fill="none" stroke="#0b8fd3" stroke-width="1.5"/><path d="M4 7l2 2 4-4" fill="none" stroke="#0b8fd3" stroke-width="1.6"/></svg>Lorem Ipsum is simply dummy text of the printing and typesetting industry.</li>
        <li><svg width="14" height="14" viewBox="0 0 14 14"><circle cx="7" cy="7" r="6" fill="none" stroke="#0b8fd3" stroke-width="1.5"/><path d="M4 7l2 2 4-4" fill="none" stroke="#0b8fd3" stroke-width="1.6"/></svg>Lorem Ipsum is simply dummy text of the printing and typesetting industry.</li>
        <li><svg width="14" height="14" viewBox="0 0 14 14"><circle cx="7" cy="7" r="6" fill="none" stroke="#0b8fd3" stroke-width="1.5"/><path d="M4 7l2 2 4-4" fill="none" stroke="#0b8fd3" stroke-width="1.6"/></svg>Lorem Ipsum is simply dummy text of the printing and typesetting industry.</li>
      </ul>
    </div>
  </section>

  <!-- services -->
  <section>
    <div class="abs services-band" role="img" aria-label="Faded background of construction workers on site"></div>
    <div class="abs center-head" style="top:1398px">
      <div class="eyebrow">What we offer</div>
      <h2 class="sec-title" style="margin-top:8px">Services</h2>
    </div>
    <div class="abs service" style="left:98px;top:1470px">
      <div class="pic" role="img" aria-label="Commercial interior with wooden tiered seating" style="background:linear-gradient(180deg,#8a7c6c,#c99a5e 60%,#e2e0dc)"></div>
      <h3>Commercial Design</h3>
      <p>Lorem Ipsum is simply dummy text of the printing and typesetting industry. Lorem Ipsum has been the industry's</p>
    </div>
    <div class="abs service" style="left:470px;top:1470px">
      <div class="pic" role="img" aria-label="Two engineers in hard hats at a steel frame build" style="background:linear-gradient(180deg,#5d86b8,#8fa9c4 50%,#c9733a)"></div>
      <h3>Development construction</h3>
      <p>Lorem Ipsum is simply dummy text of the printing and typesetting industry. Lorem Ipsum has been the industry's</p>
    </div>
    <div class="abs service" style="left:841px;top:1470px">
      <div class="pic" role="img" aria-label="Renovation plans with tools and material samples" style="background:linear-gradient(160deg,#9a9da0,#dcdad5 50%,#b88a58)"></div>
      <h3>Renovation</h3>
      <p>Lorem Ipsum is simply dummy text of the printing and typesetting industry. Lorem Ipsum has been the industry's</p>
    </div>
  </section>

  <!-- projects -->
  <section>
    <div class="abs center-head" style="top:2032px">
      <div class="eyebrow">We work</div>
      <h2 class="sec-title" style="margin-top:8px">Projects</h2>
    </div>
    <svg class="abs" style="left:0;top:2100px" width="1200" height="460" viewBox="0 0 1200 460" role="img" aria-label="Gallery of completed interiors and active job sites">
      <polygon points="292,15 444,167 292,319 140,167" fill="#8c9196"/>
      <polygon points="597,44 720,167 597,290 474,167" fill="#7a6a58"/>
      <polygon points="751,25 811,85 751,145 691,85" fill="#6d4e3a"/>
      <polygon points="903,44 1026,167 903,290 780,167" fill="#a06a32"/>
      <polygon points="751,191 874,314 751,437 628,314" fill="#8fa3b4"/>
      <polygon points="977,250 1037,310 977,370 917,310" fill="#b08a66"/>
      <polygon points="898,328 958,388 898,448 838,388" fill="#6e7f90"/>
    </svg>
    <p class="abs proj-copy">Lorem Ipsum is simply dummy text of the printing and typesetting industry. Lorem Ipsum has been the industry's</p>
    <div class="abs btn proj-btn">View all projects</div>
  </section>

  <!-- quality -->
  <section>
    <div class="abs quality-band" role="img" aria-label="Faded glass facade of a commercial building"></div>
    <div class="abs quality-copy">
      <div class="eyebrow" style="color:#222">We work</div>
      <h2 class="sec-title" style="margin-top:22px">Prove our quality</h2>
      <p>Lorem Ipsum is simply dummy text of the printing and typesetting industry. Lorem Ipsum has been the industry's standard dummy text ever since the 1500s.</p>
    </div>
    <div class="stat" style="left:59px"><div class="num">4k+</div><span>Projects<br>Done</span></div>
    <div class="stat" style="left:254px"><div class="num">4k+</div><span>Getting<br>Rewards</span></div>
    <div class="abs btn quality-btn">Get started now</div>
  </section>

  <!-- news -->
  <section>
    <div class="abs center-head" style="top:3273px">
      <div class="eyebrow">News</div>
      <h2 class="sec-title" style="margin-top:8px">Latest News</h2>
    </div>
    <article class="abs card" style="left:161px;top:3355px">
      <div class="pic" role="img" aria-label="Model of a house frame on blueprints" style="background:linear-gradient(160deg,#cfd6de,#e9e4dc 50%,#b9c7d6)"></div>
      <div class="meta"><span>📅&#xFE0E; Jan 5,2022</span><span>💬&#xFE0E; 5</span></div>
      <h3>Lorem Ipsum is simply dummy text of the printing and typesetting.</h3>
      <p>Lorem Ipsum is simply dummy text of the printing and typesetting industry. Lorem Ipsum has been the industry's</p>
    </article>
    <article class="abs card" style="left:461px;top:3355px">
      <div class="pic" role="img" aria-label="Finished commercial lounge interior" style="background:linear-gradient(180deg,#7a5a40,#c9b6a0 50%,#9a5a35)"></div>
      <div class="meta"><span>📅&#xFE0E; Jan 5,2022</span><span>💬&#xFE0E; 5</span></div>
      <h3>Lorem Ipsum is simply dummy text of the printing and typesetting.</h3>
      <p>Lorem Ipsum is simply dummy text of the printing and typesetting industry. Lorem Ipsum has been the industry's</p>
    </article>
    <article class="abs card" style="left:761px;top:3355px">
      <div class="pic" role="img" aria-label="Site crew in hard hats reviewing drawings" style="background:linear-gradient(150deg,#d7d2cb,#e0a05a 55%,#c06a3a)"></div>
      <div class="meta"><span>📅&#xFE0E; Jan 5,2022</span><span>💬&#xFE0E; 5</span></div>
      <h3>Lorem Ipsum is simply dummy text of the printing and typesetting.</h3>
      <p>Lorem Ipsum is simply dummy text of the printing and typesetting industry. Lorem Ipsum has been the industry's</p>
    </article>
  </section>

  <!-- footer -->
  <footer>
    <div class="abs footer"></div>
    <div class="abs foot-brand"><span class="mark"></span><span>DUNMORE RIDGE<br>CONSTRUCTION</span></div>
    <div class="abs foot-col" style="left:340px;top:3947px">
      <h4>Site Map</h4>
      <ul><li>- Home</li><li>- About Us</li><li>- Services</li><li>- Project</li><li>- Contact Us</li></ul>
    </div>
    <div class="abs foot-col" style="left:615px;top:3947px">
      <h4>Contact Us</h4>
      <ul class="contact-list">
        <li><svg width="14" height="16" viewBox="0 0 14 16"><path d="M7 1a5 5 0 0 1 5 5c0 4-5 9-5 9S2 10 2 6a5 5 0 0 1 5-5z" fill="none" stroke="#fff" stroke-width="1.3"/><circle cx="7" cy="6" r="1.8" fill="none" stroke="#fff" stroke-width="1.2"/></svg>101-Lorem ipsum is dummy</li>
        <li><svg width="16" height="16" viewBox="0 0 16 16"><path d="M4 1l3 4-2 2c1 2 3 4 5 5l2-2 3 3-2 2C7 15 1 9 1 3z" fill="none" stroke="#fff" stroke-width="1.3"/></svg>555 014 7890</li>
        <li><svg width="18" height="13" viewBox="0 0 18 13"><rect x="1" y="1" width="16" height="11" fill="none" stroke="#fff" stroke-width="1.3"/><path d="M1 1l8 6 8-6" fill="none" stroke="#fff" stroke-width="1.3"/></svg>info@dunmoreridge.com</li>
      </ul>
    </div>
    <div class="abs foot-col" style="left:892px;top:3947px">
      <h4>Newsletters</h4>
      <div class="news-input">ENter Email Address.....</div>
      <div class="btn news-btn">Subscribe now</div>
    </div>
    <div class="abs copyright">Copyright © DUNMORE RIDGE CONSTRUCTION 2022 All Rights Reserved.</div>
  </footer>

</div>
</body>
</html>
```